Web Design Project

We have a website in beta that needs updating and are looking for a freash new look for the Home page including Logo.
Our company is called " Pim Sa Ox " we specialize in classified advertising using video. Our consumers will be businesses selling a product or service. Please visit www.pimsaox.com
Our aim past this point is to engage a developer to write the code based on the best design. Our target market is the U.S and I have included some of the landing pages to give you a better idea of what we are trying to acheive

http://www.pimsaox.com/
http://www.pimsaox.com/cars_home.php
http://www.pimsaox.com/boats.php
http://www.pimsaox.com/electronic.php
http://www.pimsaox.com/realestate.php
http://www.pimsaox.com/roommates.php

Target Market(s)

20-35 yr old people who are connected to the internet via mobile phone and use social media on a daily/weekly basis

Industry/Entity Type

Advertising

Requirements
Must have
• We would like to use lots of images to convey it is a video driven website business
Nice to have
• Logo to incorporate same theme of website ( ie ) you are here to watch videos of thinhs to buy & sell
Should not have
• This is to be a freash new site with large type and bold fonts

```html
<!DOCTYPE html>
<html lang="en">
<head>
<meta charset="utf-8">
<title>Your Company Name – Classifieds</title>
<link rel="stylesheet" href="https://fonts.googleapis.com/css2?family=PT+Sans:wght@400;700&family=Gelasio:wght@400&family=Arimo:wght@400;700&display=swap">
<style>
:root{
  --ink:#111;
  --grey-head:#6b6b6b;
  --grey-text:#7a7a7a;
  --rule:#d6d6d6;
  --nav:#0c0c0c;
  --nav-active:#1fb4f0;
  --blue-deep:#0b4f86;
  --blue-mid:#2a8fd0;
  --blue-btn:#0a6fd6;
  --orange:#e5801a;
  --orange-dark:#c2600c;
  --green:#6cbb1e;
  --accent:#c96a1c;
  --footer:#1f1f1f;
  --footer-top:#3a3a3a;
  --red:#c20d0d;
  --white:#fff;
  --sans:"PT Sans",sans-serif;
  --body:"Arimo",sans-serif;
  --serif:"Gelasio",serif;
}
*{box-sizing:border-box;margin:0;padding:0}
html,body{width:906px;height:1200px;overflow:hidden;background:var(--white)}
body{position:relative;font-family:var(--body);color:var(--ink)}
.abs{position:absolute}

/* header */
.masthead{left:0;top:0;width:906px;height:79px;background:linear-gradient(#fafafa,#e4e4e4);border-top:4px solid #3a3a3a}
.brand{left:98px;top:28px;font-family:var(--sans);font-weight:700;font-size:24px;color:var(--ink)}
.account-links{left:736px;top:10px;font-size:9px;color:#333}
.post-ad{left:695px;top:45px;width:111px;height:28px;border-radius:4px;background:linear-gradient(#2b8cf0,var(--blue-btn));color:var(--white);font-family:var(--sans);font-size:12px;display:flex;align-items:center;justify-content:center;gap:6px}

/* hero band */
.hero-band{left:0;top:79px;width:906px;height:357px;background:radial-gradient(ellipse at 50% 35%,#5fb2e6 0%,var(--blue-mid) 40%,var(--blue-deep) 100%)}
.main-nav{left:97px;top:79px;width:710px;height:27px;background:var(--nav);border-radius:0 0 6px 6px;display:flex;align-items:center;padding-left:28px;font-family:var(--sans);font-size:11px;color:var(--white)}
.main-nav span{padding:0 19px;border-right:1px solid #555;line-height:13px}
.main-nav span:first-child{padding-left:0;color:var(--nav-active)}
.main-nav span:nth-child(7){border-right:none}
.social{display:flex;gap:3px;margin-left:auto;margin-right:14px}
.social i{width:12px;height:12px;background:#9a9a9a;border-radius:2px}
.slider{left:94px;top:120px;width:714px;height:275px;border-radius:10px;border:2px solid #7cc0ea;background:linear-gradient(90deg,var(--orange-dark),var(--orange) 50%,#d86f10);overflow:hidden}
.slide-photo{position:absolute;left:240px;top:0;width:474px;height:275px;background:linear-gradient(100deg,rgba(230,128,26,0) 0%,rgba(80,60,50,.35) 55%,#2a2a2e 80%,#ddd 100%)}
.welcome{left:116px;top:155px;width:210px;height:240px;background:linear-gradient(#2a1a10,#3a2414 70%,var(--orange-dark));border-radius:8px 8px 0 0;padding:22px 12px 0 13px;color:var(--white)}
.welcome h2{font-family:var(--serif);font-weight:400;font-size:19px;margin-bottom:10px}
.welcome p{font-size:8.6px;line-height:12.6px;margin-bottom:11px}
.shop-now{left:147px;top:338px;width:148px;height:30px;border-radius:15px;background:linear-gradient(#8fd63a,var(--green));color:var(--white);font-family:var(--sans);font-weight:700;font-size:13px;display:flex;align-items:center;justify-content:center;gap:14px}
.dots{left:744px;top:405px;display:flex;gap:4px}
.dots i{width:9px;height:9px;background:var(--white)}
.dots i:first-child{background:#8be01e}

/* search */
.field{top:455px;width:197px;height:34px;border:1px solid var(--rule);border-radius:6px;font-size:8.5px;color:#999;padding:12px 8px;background:var(--white)}
.field svg{position:absolute;right:8px;top:13px}
.search-btn{left:717px;top:455px;width:90px;height:34px;border-radius:6px;background:linear-gradient(#666,#2b2b2b);color:var(--white);font-size:9px;display:flex;align-items:center;justify-content:center}

/* listings */
.section-title{left:97px;top:522px;font-family:var(--sans);font-weight:700;font-size:19px;color:var(--grey-head)}
.ad-card{width:165px;height:142px;border:1px solid var(--rule);border-radius:3px;background:var(--white)}
.ad-photo{position:absolute;left:7px;top:7px;width:151px;height:80px;border:1px solid #555}
.ad-card h3{position:absolute;left:8px;top:95px;font-family:var(--sans);font-weight:700;font-size:11px;color:var(--accent)}
.ad-card p{position:absolute;left:8px;top:110px;width:150px;font-size:8px;line-height:10.5px;color:var(--grey-text)}
.sidebar{left:634px;top:556px;width:173px;height:299px;border:1px solid var(--rule);border-radius:3px;padding:8px 8px}
.sidebar h4{font-family:var(--sans);font-weight:400;font-size:15px;color:#444}
.sidebar p{font-size:8px;line-height:11px;color:var(--grey-text);margin-top:3px}
.sidebar .who{font-size:9px;color:#555;margin-top:2px}
.divider{height:10px;margin:7px 0;background:radial-gradient(ellipse at 50% 0,#bbb 0,rgba(255,255,255,0) 60%)}
.input{border:1px solid #aaa;font-size:8.5px;color:#555;padding:2px 4px;margin-top:4px}
.submit{margin:10px 0 0 auto;width:48px;height:12px;background:#222;color:var(--white);font-size:9px;text-align:center;line-height:12px}

/* steps */
.steps{left:0;top:868px;width:906px;height:193px;background:linear-gradient(#f6f6f6,#dcdcdc);border-top:1px solid #e2e2e2}
.step{top:887px;width:206px;height:170px;text-align:center}
.step svg{display:block}
.step-art{position:absolute;left:55px;top:35px;width:96px;height:55px;border-radius:6px}
.step-label{position:absolute;left:0;top:140px;width:206px;font-family:var(--sans);font-weight:700;font-size:19px;color:#555}

/* footer */
.footer{left:0;top:1061px;width:906px;height:139px;background:linear-gradient(var(--footer-top),var(--footer));color:var(--white)}
.footer-col{top:1073px}
.footer-col h5{font-family:var(--sans);font-weight:700;font-size:12px;margin-bottom:9px}
.footer-col li{list-style:none;font-size:7.5px;line-height:14.4px}
.subscribe-input{left:591px;top:1101px;width:165px;height:19px;background:var(--white);border-radius:3px}
.subscribe-btn{left:761px;top:1101px;width:45px;height:19px;background:var(--red);font-size:8.5px;display:flex;align-items:center;justify-content:center;border-radius:2px}
.rights{left:615px;top:1159px;font-size:8.5px;color:#ddd}
</style>
</head>
<body>

<header>
  <div class="abs masthead"></div>
  <div class="abs brand">Your Company Name</div>
  <div class="abs account-links">Sign in &nbsp;/&nbsp; Register</div>
  <div class="abs post-ad">POST AN ADD
    <svg width="10" height="9" viewBox="0 0 10 9"><path d="M1 1l3.5 3.5L1 8M5 1l3.5 3.5L5 8" stroke="#fff" stroke-width="1.4" fill="none"/></svg>
  </div>
</header>

<section>
  <div class="abs hero-band"></div>
  <nav class="abs main-nav">
    <span>Home</span><span>Cars</span><span>Electronics</span><span>Real Estate</span><span>Roommates</span><span>Other Categories</span><span>My Account</span>
    <div class="social"><i></i><i></i><i></i><i></i><i></i></div>
  </nav>
  <div class="abs slider">
    <div class="slide-photo" role="img" aria-label="Businessman in a suit holding out a payment card above a row of figures pushing shopping carts"></div>
  </div>
  <div class="abs welcome">
    <h2>Welcome</h2>
    <p>Lorem ipsum dolor sit amet, consectetuer adipiscing elit, sed diam nonummy nibh euisd tincidunt ut laoreet dolore magna aliquam eravolut­pat. Ut wisi enim ad minim veniam.</p>
    <p>quis nostud exerci tation ullamcorper suscipit lobortis nsl ut aliquip ex ea commodo consequat.</p>
  </div>
  <div class="abs shop-now">Shop Now
    <svg width="18" height="18" viewBox="0 0 18 18"><circle cx="9" cy="9" r="7.5" stroke="#fff" stroke-width="1.5" fill="none"/><path d="M5 9h7M9 6l3 3-3 3" stroke="#fff" stroke-width="1.5" fill="none"/></svg>
  </div>
  <div class="abs dots"><i></i><i></i><i></i><i></i></div>
</section>

<section>
  <div class="abs field" style="left:97px">I'm looking for ...<svg width="12" height="9"><path d="M0 0h12L6 9z" fill="#888"/></svg></div>
  <div class="abs field" style="left:304px">Search by Categories ...<svg width="12" height="9"><path d="M0 0h12L6 9z" fill="#888"/></svg></div>
  <div class="abs field" style="left:510px">In Country ...<svg width="12" height="9"><path d="M0 0h12L6 9z" fill="#888"/></svg></div>
  <div class="abs search-btn">Search</div>
</section>

<section>
  <h2 class="abs section-title">RECENT ADDS</h2>

  <article class="abs ad-card" style="left:97px;top:556px">
    <div class="ad-photo" role="img" aria-label="Red sports car" style="background:linear-gradient(135deg,#2a2a2a,#8a1010 50%,#c8c8c8)"></div>
    <h3>LOREM</h3><p>Lorem ipsum dolor sit amet, consectetur adipiscing eleiuelit, sed do......</p>
  </article>
  <article class="abs ad-card" style="left:275px;top:556px">
    <div class="ad-photo" role="img" aria-label="Yellow sport motorbike" style="background:linear-gradient(135deg,#b8b8b8,#b9b431 50%,#555)"></div>
    <h3>LOREM</h3><p>Lorem ipsum dolor sit amet, consectetur adipiscing eleiuelit, sed do......</p>
  </article>
  <article class="abs ad-card" style="left:454px;top:556px">
    <div class="ad-photo" role="img" aria-label="Home theatre speaker set" style="background:linear-gradient(135deg,#fff,#4a2a35 50%,#ddd)"></div>
    <h3>LOREM</h3><p>Lorem ipsum dolor sit amet, consectetur adipiscing eleiuelit, sed do......</p>
  </article>
  <article class="abs ad-card" style="left:97px;top:713px">
    <div class="ad-photo" role="img" aria-label="Two-storey house with orange roof" style="background:linear-gradient(#8fc6ea,#d98a4a 45%,#e8e0d2 75%,#6a9a5a)"></div>
    <h3>LOREM</h3><p>Lorem ipsum dolor sit amet, consectetur adipiscing eleiuelit, sed do......</p>
  </article>
  <article class="abs ad-card" style="left:275px;top:713px">
    <div class="ad-photo" role="img" aria-label="Desktop computer with monitor and keyboard" style="background:linear-gradient(135deg,#fff,#2a2a2a 55%,#eee)"></div>
    <h3>LOREM</h3><p>Lorem ipsum dolor sit amet, consectetur adipiscing eleiuelit, sed do......</p>
  </article>
  <article class="abs ad-card" style="left:454px;top:713px">
    <div class="ad-photo" role="img" aria-label="Orange and white motor boat" style="background:linear-gradient(#fff,#e07a20 45%,#777 70%,#fff)"></div>
    <h3>LOREM</h3><p>Lorem ipsum dolor sit amet, consectetur adipiscing eleiuelit, sed do......</p>
  </article>

  <aside class="abs sidebar">
    <h4>News</h4>
    <p>Lorem ipsum dolor sit amet, consectetur adipiscing elit,....</p>
    <div class="who">8/June</div>
    <div class="divider"></div>
    <h4>Testimonails</h4>
    <p>Lorem ipsum dolor sit amet, consectetur adipiscing elit,....</p>
    <div class="who">John</div>
    <div class="divider"></div>
    <h4>Contact us</h4>
    <div class="input" style="height:18px">Email</div>
    <div class="input" style="height:46px">Message</div>
    <div class="submit">SUBMIT</div>
  </aside>
</section>

<section>
  <div class="abs steps"></div>
  <div class="abs step" style="left:101px">
    <svg width="206" height="125" viewBox="0 0 206 125"><path d="M40 110C10 110 2 85 18 72 4 55 20 30 45 36 50 10 85 4 100 20 115 2 155 8 158 32 190 28 204 58 188 74 204 92 184 118 158 110 145 124 110 124 100 112 85 124 55 122 40 110Z" fill="#fff" stroke="#777" stroke-width="1.2"/></svg>
    <div class="step-art" role="img" aria-label="Video camcorder with flip-out screen" style="background:linear-gradient(135deg,#999,#3a3a3a)"></div>
    <div class="step-label">CREAT IT</div>
  </div>
  <div class="abs step" style="left:349px">
    <svg width="206" height="125" viewBox="0 0 206 125"><path d="M40 110C10 110 2 85 18 72 4 55 20 30 45 36 50 10 85 4 100 20 115 2 155 8 158 32 190 28 204 58 188 74 204 92 184 118 158 110 145 124 110 124 100 112 85 124 55 122 40 110Z" fill="#fff" stroke="#777" stroke-width="1.2"/></svg>
    <div class="step-art" role="img" aria-label="Blue folder resting on a small cloud" style="background:linear-gradient(#6fb0e6,#9fd0f4)"></div>
    <div class="step-label">UPLOAD IT</div>
  </div>
  <div class="abs step" style="left:597px">
    <svg width="206" height="125" viewBox="0 0 206 125"><path d="M40 110C10 110 2 85 18 72 4 55 20 30 45 36 50 10 85 4 100 20 115 2 155 8 158 32 190 28 204 58 188 74 204 92 184 118 158 110 145 124 110 124 100 112 85 124 55 122 40 110Z" fill="#fff" stroke="#777" stroke-width="1.2"/></svg>
    <div class="step-art" role="img" aria-label="Handshake between two people in suits" style="background:linear-gradient(90deg,#2a2a2a,#c99a80 50%,#2a2a2a)"></div>
    <div class="step-label">SELL IT</div>
  </div>
</section>

<footer>
  <div class="abs footer"></div>
  <div class="abs footer-col" style="left:98px"><h5>BUY / BROWSE</h5><ul><li>Roommates</li><li>Cars</li><li>Boats</li><li>Electronics</li><li>Others</li></ul></div>
  <div class="abs footer-col" style="left:231px"><h5>SELL</h5><ul><li>Start Selling</li><li>Login</li><li>Shooting Video</li><li>Uploading Video</li><li>Buying</li></ul></div>
  <div class="abs footer-col" style="left:351px"><h5>INFO</h5><ul><li>VBlog</li><li>FAQs</li><li>Terms of Use</li><li>Privacy Policy</li><li>Buyer/Seller Safety</li></ul></div>
  <div class="abs footer-col" style="left:467px"><h5>CONTACT</h5><ul><li>Contact Us</li><li>Feedback Form</li><li>Referral Program</li><li>Subscription</li></ul></div>
  <div class="abs footer-col" style="left:591px"><h5>SUBSCRIBE FOR NEWS LETTERS</h5></div>
  <div class="abs subscribe-input"></div>
  <div class="abs subscribe-btn">Submit</div>
  <div class="abs rights">All rights reserved</div>
</footer>

</body>
</html>
```